Lantern of Renewal needs a business card design

I need a business card design for my company to promote my new Christian non-fiction book, "Where The River Bends Home." I also want it to promote my web site, www.lanternofrenewalbks.com. The book is about empowering people to be transformed through a deeper relationship with God. I am picturing a design with a dove over water that matches the colors of my book cover, blue, white, yellow, and orange. Fire and light would also be possible elements of the design. I would like to be able to use the dove by itself as a logo for my business. This is my first book and I do not know if others will follow. The name of my publishing company is Silver Harvest Press, named after Gideon in the Bible story from the book of Judges. My book was independently published and was recently selected as a finalist for the 2015 Bright Horizon SMALLPRESS book award in the Christian non-fiction genre.

Target Market(s)

People who are hungry for more of God and who want to experience deep change in their lives.

Industry/Entity Type

Business

Contact Information for Business Card

Dana Whitcombe
Author
Where The River Bends Home
4287 Maple Orchard Lane
Austin, Texas 78651-2097
512-555-0143 512-555-0178
dana-whitcombe@examplemail.net
www.lanternofrenewalbks.com

Colors
0355a3
3377b5
85acd3
cedeed
fbee3e
ffc214

Requirements
Must have
• A dove with a blue background, peaceful and appealing
Nice to have
• Water and fire or light
Should not have
• Violence or fear-producing images

```html
<!DOCTYPE html>
<html lang="en">
<head>
<meta charset="utf-8">
<title>Lantern of Renewal — Business Card</title>
<link rel="stylesheet" href="https://fonts.googleapis.com/css2?family=Tinos:wght@400;700&family=Great+Vibes&display=swap">
<style>
  :root {
    --page-bg: #e9edf1;
    --card-bg: #ffffff;
    --navy: #0b2e6b;
    --ink: #0f2346;
    --brand-blue: #0355a3;
    --mid-blue: #3377b5;
    --soft-blue: #85acd3;
    --pale-blue: #cedeed;
    --gold: #ffc214;
    --gold-dark: #9a6a00;
  }
  * { margin: 0; padding: 0; box-sizing: border-box; }
  html, body {
    width: 1200px; height: 782px; overflow: hidden;
    background: var(--page-bg);
  }
  .card {
    position: absolute; left: 40px; top: 61px;
    width: 1120px; height: 660px;
    background: var(--card-bg);
    overflow: hidden;
    font-family: "Tinos", "Times New Roman", serif;
    box-shadow: 0 2px 6px rgba(0,0,0,0.12);
  }
  .water-art { position: absolute; left: 0; top: 0; width: 1120px; height: 660px; }
  .brand {
    position: absolute; left: 100px; top: 50px; width: 270px;
    text-align: center;
  }
  .brand-mark {
    width: 64px; height: 64px; border-radius: 50%;
    background: var(--mid-blue); margin: 0 auto 48px;
  }
  .brand-name { font-size: 21px; color: var(--ink); line-height: 1; }
  .author-block {
    position: absolute; left: 611px; top: 88px; width: 440px;
    text-align: center;
  }
  .author-name { font-size: 33px; font-weight: 700; color: var(--navy); line-height: 1.15; }
  .author-role { font-size: 28px; color: var(--ink); line-height: 1.2; }
  .book-title {
    margin-top: 14px; font-size: 34px; font-weight: 700; letter-spacing: 0.5px;
    color: #ffffff; -webkit-text-stroke: 1.6px var(--mid-blue);
    line-height: 1.1; white-space: nowrap;
  }
  .book-title-script {
    font-family: "Great Vibes", cursive; font-size: 58px;
    color: var(--gold); -webkit-text-stroke: 0.8px var(--gold-dark);
    line-height: 1.1; white-space: nowrap;
  }
  .contact-list {
    position: absolute; left: 56px; top: 352px; list-style: none;
  }
  .contact-item {
    display: flex; align-items: center; height: 46px;
    font-size: 29px; color: var(--ink); white-space: nowrap;
  }
  .contact-icon { width: 30px; height: 30px; margin-right: 14px; flex: none; }
  .contact-icon * { fill: none; stroke: var(--ink); stroke-width: 2; }
  .contact-icon .solid { fill: var(--ink); stroke: none; }
</style>
</head>
<body>
<div class="card">
  <svg class="water-art" viewBox="0 0 1120 660" role="img" aria-label="Illustration of a clear blue water wave with bubbles and sparkles filling the lower card">
    <defs>
      <linearGradient id="waterTone" x1="0" y1="0" x2="1" y2="1">
        <stop offset="0" stop-color="#cedeed"/>
        <stop offset="0.45" stop-color="#85acd3"/>
        <stop offset="1" stop-color="#0355a3"/>
      </linearGradient>
    </defs>
    <path d="M0,285 C90,250 200,225 300,250 C430,285 520,350 660,362 C820,375 960,330 1120,282 L1120,660 L0,660 Z" fill="url(#waterTone)"/>
  </svg>

  <div class="brand">
    <div class="brand-mark"></div>
    <p class="brand-name">Lantern of Renewal</p>
  </div>

  <div class="author-block">
    <p class="author-name">Dana Whitcombe</p>
    <p class="author-role">Author</p>
    <p class="book-title">WHERE THE RIVER</p>
    <p class="book-title-script">Bends Home</p>
  </div>

  <ul class="contact-list">
    <li class="contact-item">
      <svg class="contact-icon" viewBox="0 0 30 30"><rect x="9" y="3" width="13" height="24" rx="2"/><line x1="13" y1="23" x2="18" y2="23"/></svg>
      78651-2097
    </li>
    <li class="contact-item">
      <svg class="contact-icon" viewBox="0 0 30 30"><path class="solid" d="M8 3 L12 3 L14 10 L11 12 C12 16 14 18 18 19 L20 16 L27 18 L27 22 C26 26 22 27 19 26 C11 23 6 18 4 10 C3 7 5 3 8 3 Z"/></svg>
      512-555-0143
    </li>
    <li class="contact-item">
      <svg class="contact-icon" viewBox="0 0 30 30"><rect x="8" y="3" width="14" height="9"/><rect x="3" y="12" width="24" height="12" rx="2"/><rect x="8" y="20" width="14" height="7"/></svg>
      512-555-0178
    </li>
    <li class="contact-item">
      <svg class="contact-icon" viewBox="0 0 30 30"><rect x="3" y="7" width="24" height="16"/><polyline points="3,7 15,17 27,7"/></svg>
      dana-whitcombe@examplemail.net
    </li>
    <li class="contact-item">
      <svg class="contact-icon" viewBox="0 0 30 30"><circle cx="15" cy="15" r="12"/><ellipse cx="15" cy="15" rx="5" ry="12"/><line x1="3" y1="15" x2="27" y2="15"/><line x1="5" y1="9" x2="25" y2="9"/><line x1="5" y1="21" x2="25" y2="21"/></svg>
      www.lanternofrenewalbks.com
    </li>
    <li class="contact-item">
      <svg class="contact-icon" viewBox="0 0 30 30"><path class="solid" d="M15 3 L28 13 L2 13 Z"/><rect class="solid" x="5" y="14" width="20" height="13"/><rect x="12" y="18" width="6" height="9" fill="#ffffff" stroke="none"/></svg>
      4287 Maple Orchard Lane Austin, Texas
    </li>
  </ul>
</div>
</body>
</html>
```